Business card and e-mail signature template.

I need a business card- and e-mail signature template for a project (signature will be used with gmail). The logo is attached.

There the logo has a focus on the “Lumora” part of the name. The URL for the project is www.lumorafest.com.
The full name of the project is The Lumora Expo. The project will be publicly known as “Lumora” or “Lumora2020”. In all documents we will present the project as Lumora2020.

The logo can contain design elements and the design should be modern and appealing to both young people and traditional companies.

This competition is part of a bigger delivery. The winner will therefore be a strong candidate for the brand guide og maybe website.

```html
<!DOCTYPE html>
<html lang="en">
<head>
<meta charset="utf-8">
<title>Lumora2020 – Business Card</title>
<link href="https://fonts.googleapis.com/css2?family=Montserrat:wght@500;600&family=Open+Sans:wght@400;600&display=swap" rel="stylesheet">
<style>
  :root{
    --stage:#1f1f21;
    --card:#f1f1f1;
    --card-shade:#e2e2e2;
    --panel:#fafafa;
    --row:#ececec;
    --teal:#16b2b4;
    --pink:#e0185e;
    --orange:#f28a26;
    --ink:#2b2b2b;
    --logo-ink:#555559;
  }
  *{margin:0;padding:0;box-sizing:border-box}
  html,body{width:1200px;height:900px;overflow:hidden;background:var(--stage)}
  .stage{position:relative;width:1200px;height:900px}

  .card{position:absolute;width:620px;height:354px;border-radius:22px;overflow:hidden;
        background:linear-gradient(160deg,#fbfbfb,var(--card) 55%,var(--card-shade));
        box-shadow:0 18px 40px rgba(0,0,0,.45)}
  .card--front{left:70px;top:70px}
  .card--back{left:510px;top:476px}

  .stripe{position:absolute;left:0;right:0;height:14px;display:flex}
  .stripe--top{top:0}
  .stripe--bottom{bottom:0}
  .stripe span{height:100%}
  .c-teal{background:var(--teal)}
  .c-pink{background:var(--pink)}
  .c-orange{background:var(--orange)}

  .wordmark{position:absolute;display:flex;align-items:center;gap:14px;white-space:nowrap;
            font-family:"Montserrat",sans-serif;font-weight:600;color:var(--logo-ink);letter-spacing:1px}
  .wordmark__dot{border-radius:50%;background:var(--pink);flex:none}
  .card--front .wordmark{left:50%;top:50%;transform:translate(-50%,-50%);font-size:44px}
  .card--front .wordmark__dot{width:34px;height:34px}
  .card--back .wordmark{left:0;width:290px;top:160px;justify-content:center;gap:10px;font-size:24px}
  .card--back .wordmark__dot{width:20px;height:20px}

  .details{position:absolute;left:290px;top:0;width:330px;height:100%;background:var(--panel);
           box-shadow:-6px 0 14px rgba(0,0,0,.08);font-family:"Open Sans",sans-serif;color:var(--ink)}
  .details__head{position:absolute;left:0;right:0;top:30px;height:64px;background:var(--pink);
                 color:#fff;padding:9px 22px}
  .details__name{font-size:22px;font-weight:600;letter-spacing:.5px;line-height:1.1}
  .details__role{font-size:13px;letter-spacing:.5px;opacity:.92}
  .tabs{position:absolute;right:0;top:94px;width:18px}
  .tabs span{display:block;height:18px}
  .details__address{position:absolute;left:18px;top:114px;font-size:13.5px}
  .contact{position:absolute;left:0;right:0;height:36px;display:flex;align-items:center;font-size:14px}
  .contact:nth-of-type(odd){background:var(--row)}
  .contact__icon{width:34px;height:36px;display:flex;align-items:center;justify-content:center;margin-right:14px}
  .contact__icon svg{width:16px;height:16px;fill:#fff}
  .contact--phone{top:150px}
  .contact--mail{top:190px}
  .contact--web{top:230px}
</style>
</head>
<body>
<main class="stage">

  <section class="card card--front" aria-label="Business card front">
    <div class="stripe stripe--top"><span class="c-teal" style="width:24%"></span><span class="c-pink" style="width:36%"></span><span class="c-orange" style="width:40%"></span></div>
    <div class="wordmark"><span class="wordmark__dot"></span>LUMORA2020</div>
    <div class="stripe stripe--bottom"><span class="c-teal" style="width:34%"></span><span class="c-pink" style="width:36%"></span><span class="c-orange" style="width:30%"></span></div>
  </section>

  <section class="card card--back" aria-label="Business card back">
    <div class="wordmark"><span class="wordmark__dot"></span>LUMORA2020</div>
    <div class="details">
      <div class="details__head">
        <p class="details__name">MIRA SOLEN</p>
        <p class="details__role">CEO/FOUNDER</p>
      </div>
      <div class="tabs"><span class="c-teal"></span><span class="c-pink"></span><span class="c-orange"></span></div>
      <p class="details__address">PO Box 2210 Fairview,OR 97024</p>
      <div class="contact contact--phone">
        <span class="contact__icon c-teal"><svg viewBox="0 0 24 24"><path d="M6.6 10.8a15 15 0 0 0 6.6 6.6l2.2-2.2c.3-.3.7-.4 1-.2 1.1.4 2.3.6 3.6.6.6 0 1 .4 1 1V20c0 .6-.4 1-1 1A17 17 0 0 1 3 4c0-.6.4-1 1-1h3.5c.6 0 1 .4 1 1 0 1.3.2 2.5.6 3.6.1.3 0 .7-.2 1z"/></svg></span>
        000-0000-0000
      </div>
      <div class="contact contact--mail">
        <span class="contact__icon c-pink"><svg viewBox="0 0 24 24"><path d="M3 5h18c.6 0 1 .4 1 1v12c0 .6-.4 1-1 1H3c-.6 0-1-.4-1-1V6c0-.6.4-1 1-1zm9 7.5L4.5 7.5v1.8L12 14.3l7.5-5V7.5z"/></svg></span>
        info@lumora2020.com
      </div>
      <div class="contact contact--web">
        <span class="contact__icon c-orange"><svg viewBox="0 0 24 24"><path d="M12 2a10 10 0 1 0 0 20 10 10 0 0 0 0-20zm6.9 6h-3a15 15 0 0 0-1.3-3.6A8 8 0 0 1 18.9 8zM12 4c.8 1.2 1.5 2.5 1.9 4h-3.8c.4-1.5 1.1-2.8 1.9-4zM4.3 14a8 8 0 0 1 0-4h3.4a16 16 0 0 0 0 4zm.8 2h3a15 15 0 0 0 1.3 3.6A8 8 0 0 1 5.1 16zm3-8h-3a8 8 0 0 1 4.3-3.6C8.8 5.5 8.4 6.7 8.1 8zM12 20c-.8-1.2-1.5-2.5-1.9-4h3.8c-.4 1.5-1.1 2.8-1.9 4zm2.3-6H9.7a14 14 0 0 1 0-4h4.6a14 14 0 0 1 0 4zm.3 5.6c.6-1.1 1-2.3 1.3-3.6h3a8 8 0 0 1-4.3 3.6zm1.7-5.6a16 16 0 0 0 0-4h3.4a8 8 0 0 1 0 4z"/></svg></span>
        www.lumorafest.com
      </div>
    </div>
  </section>

</main>
</body>
</html>
```